Residential Construction Business - Site Signage

I need a design made for a site fence banner. We have a logo and branding so the design would need to be aligned with this. It would need to be made to specific size ratio so that it can be sent to the maker for production.
ratio : 4600 wide x 1700 high
The design should feature our website and also the slogan
"STAY HOME, REINVENT IT"

Target Market(s)

potential clients

Industry/Entity Type

construction

Font styles to use
Other font styles liked:
• to match branding

Colors
0054AA
0677BA
7BADD7
CADEEF
E8F1F8

Requirements
Must have
• www.velmbuild.com.au Majority of the sign is our brand logo
Nice to have
• Majority of the sign is our brand logo
Should not have
• colors and themes that arent brand relevant

```html
<!DOCTYPE html>
<html lang="en">
<head>
<meta charset="UTF-8">
<title>Velm Build – Site Fence Banner</title>
<link href="https://fonts.googleapis.com/css2?family=Poppins:wght@400;500;700&display=swap" rel="stylesheet">
<style>
  :root {
    --backdrop: #e8e8e8;
    --paper: #f6f6f7;
    --navy-top: #0c3457;
    --navy-bottom: #1a4c70;
    --ink-light: #f4f5f7;
  }
  html, body {
    margin: 0;
    padding: 0;
    width: 1200px;
    height: 704px;
    overflow: hidden;
    background: var(--backdrop);
  }
  .canvas {
    position: relative;
    width: 1200px;
    height: 704px;
  }
  .banner {
    position: absolute;
    left: 30px;
    top: 129px;
    width: 1140px;
    height: 446px;
    background: var(--paper);
    overflow: hidden;
    font-family: "Poppins", sans-serif;
  }
  .banner__field {
    position: absolute;
    inset: 0;
    width: 100%;
    height: 100%;
  }
  .brand-name {
    position: absolute;
    left: 250px;
    top: 196px;
    margin: 0;
    font-size: 42px;
    font-weight: 500;
    letter-spacing: 0.2em;
    line-height: 1;
    color: var(--ink-light);
    white-space: nowrap;
  }
  .divider {
    position: absolute;
    left: 642px;
    top: 122px;
    width: 2px;
    height: 191px;
    background: var(--ink-light);
  }
  .slogan {
    position: absolute;
    left: 684px;
    top: 124px;
    margin: 0;
    font-size: 57px;
    font-weight: 700;
    line-height: 57px;
    letter-spacing: 0.02em;
    color: var(--ink-light);
    white-space: nowrap;
  }
  .website {
    position: absolute;
    left: 686px;
    top: 278px;
    margin: 0;
    font-size: 27px;
    font-weight: 400;
    letter-spacing: 0.05em;
    color: var(--ink-light);
    white-space: nowrap;
  }
  .website strong {
    font-weight: 700;
  }
</style>
</head>
<body>
<div class="canvas">
  <section class="banner" aria-label="Velm Build site fence banner">
    <svg class="banner__field" viewBox="0 0 1140 446" preserveAspectRatio="none" aria-hidden="true">
      <defs>
        <linearGradient id="navyField" x1="0" y1="0" x2="0" y2="1">
          <stop offset="0" style="stop-color:#0c3457"/>
          <stop offset="1" style="stop-color:#1a4c70"/>
        </linearGradient>
      </defs>
      <path d="M393 0 H1140 V446 H396 L230 244 Q220 222 230 200 Z" fill="url(#navyField)"/>
    </svg>
    <h1 class="brand-name">VELM BUILD</h1>
    <div class="divider"></div>
    <p class="slogan">STAY HOME,<br>REINVENT IT</p>
    <p class="website">www.<strong>velmbuild</strong>.com.au</p>
  </section>
</div>
</body>
</html>
```